Maple Thistlewood - New monument signage for our apartment community

We have a monument sign that we would like to replace with a fresh, clean, and easy to read new design. I've included a couple pictures of the physical sign - people will be seeing this while driving very fast. It needs to be simple and easy to quickly see while driving.

* Maple Thistlewood
* Newly Renovated!
* www.maplethistlewoodhomes.example
* 555 - 318 - 7906

Suggestions:
* Bright colors
* Bold fonts
* Focus on phone number being easy to read

*** I attached a picture of something similar we did at one of our other apartment communities (Ferncliff townhomes)

Maple Thistlewood Apartment Community

```html
<!DOCTYPE html>
<html lang="en">
<head>
<meta charset="utf-8">
<title>Maple Thistlewood – Monument Sign</title>
<link rel="stylesheet" href="https://fonts.googleapis.com/css2?family=Roboto:wght@700;900&family=Kaushan+Script&display=swap">
<style>
  :root {
    --backdrop: #e9ebee;
    --frame: #2b2c2e;
    --panel: #050505;
    --signal-yellow: #f7ec15;
    --ink: #0a0a0a;
    --white: #ffffff;
    --arrow-red: #ec2227;
  }
  * { box-sizing: border-box; margin: 0; padding: 0; }
  html, body {
    width: 1200px;
    height: 1000px;
    overflow: hidden;
    background: var(--backdrop);
  }
  .canvas {
    width: 1200px;
    height: 1000px;
    display: flex;
    align-items: center;
    justify-content: center;
  }
  .sign {
    width: 1100px;
    height: 600px;
    border: 16px solid var(--frame);
    background: var(--panel);
    display: flex;
    flex-direction: column;
  }
  .sign__name {
    height: 150px;
    display: flex;
    align-items: center;
    justify-content: center;
    font-family: "Roboto", "Arial Black", sans-serif;
    font-weight: 900;
    font-size: 80px;
    letter-spacing: 1px;
    color: var(--white);
    text-transform: uppercase;
    white-space: nowrap;
  }
  .sign__band {
    height: 160px;
    background: var(--signal-yellow);
    display: flex;
    align-items: center;
    justify-content: space-between;
    padding: 0 36px 0 56px;
  }
  .sign__tagline {
    font-family: "Kaushan Script", cursive;
    font-size: 84px;
    color: var(--ink);
    transform: rotate(-3deg);
    line-height: 1;
    white-space: nowrap;
  }
  .sign__arrow { width: 170px; height: 110px; flex: none; }
  .sign__contact {
    flex: 1;
    display: flex;
    align-items: center;
    justify-content: center;
    padding: 0 36px;
    gap: 28px;
  }
  .phone-badge { width: 170px; height: 170px; flex: none; }
  .contact-lines {
    display: flex;
    flex-direction: column;
    align-items: center;
  }
  .contact-lines__phone {
    font-family: "Roboto", "Arial Black", sans-serif;
    font-weight: 900;
    font-size: 112px;
    line-height: 1;
    color: var(--white);
    letter-spacing: 2px;
    white-space: nowrap;
  }
  .contact-lines__web {
    font-family: "Roboto", Arial, sans-serif;
    font-weight: 700;
    font-size: 44px;
    line-height: 1.3;
    color: var(--white);
    white-space: nowrap;
  }
</style>
</head>
<body>
<main class="canvas">
  <section class="sign" aria-label="Maple Thistlewood monument sign">
    <h1 class="sign__name">Maple Thistlewood</h1>
    <div class="sign__band">
      <p class="sign__tagline">Newly Renovated!</p>
      <svg class="sign__arrow" viewBox="0 0 170 110" aria-hidden="true">
        <path d="M8 55 H140 M100 15 L148 55 L100 95" fill="none" stroke="var(--arrow-red)" stroke-width="20" stroke-linecap="square" stroke-linejoin="miter"/>
      </svg>
    </div>
    <div class="sign__contact">
      <svg class="phone-badge" viewBox="0 0 180 180" aria-hidden="true">
        <path d="M90 12 A78 78 0 1 0 165 68 L176 20 L138 40 A78 78 0 0 0 90 12 Z" fill="var(--signal-yellow)"/>
        <path d="M62 48 C54 52 48 60 50 74 C56 104 80 128 108 136 C120 138 130 132 134 124 L118 106 C114 102 108 104 104 108 L98 112 C84 104 74 94 68 80 L74 74 C78 70 80 64 76 60 Z" fill="var(--ink)"/>
      </svg>
      <div class="contact-lines">
        <p class="contact-lines__phone">555-318-7906</p>
        <p class="contact-lines__web">maplethistlewoodhomes.example</p>
      </div>
    </div>
  </section>
</main>
</body>
</html>
```